Basis-Buchdesign für eine Buchserie
Zielgruppe
Privatperson. Ich möchte Bücher zu Themen schreiben, die uns alle bewegen, wo aber alles schiefläuft.
Aufgabenstellung
Buchserie
Mein Kopf ist voller Gedanken, ich will all das nun niederschreiben. Ich habe bereits ein Buch geschrieben. Da ich aber dabei anonym sein musste, konnte ich keine Werbung schalten, nur sehr wenige Exemplare wurden verkauft.
Mir geht es aber gar nicht ums Geld. Ich will einfach das niederschreiben, was gesagt werden muss. Aber diesmal unter meinem echten Namen. Es sind mehrere Oberthemen, die mich interessieren. Für jedes dieser Themen möchte ich ein eigenes Buch schreiben.
Da es mehrere Bücher sein sollen, muss das „Basisdesign“ für alle Bücher gleich sein. Jedes einzelne Thema wird dann zusätzlich mit eigenen Schwerpunkten hervorgehoben, ein Überlagern, ein Ergänzen usw. des Basisdesigns findet statt.
Das Fundament fürs Basisdesign sind meine Grundgedanken, welche die heutige Zeit beschreiben: Frustration, Ohnmacht, Hoffnungslosigkeit, Untergangsszenario, …
Es geht darum, dass derzeit alles auf der Welt nicht normal verläuft. Kaum ein Land wird von einem normalen Demokraten geführt, überall gewinnen ausschließlich Nazis und Vollidioten. Im Kern der Gesellschaft gibt es keinen Zusammenhalt mehr, die durchschnittliche Intelligenz sinkt, Dumme und Idioten haben Hochkonjunktur.
Die Themen, die ich aus heutiger Sicht angehen will, sind:
- Justiz/Polizei/Gesellschaft im Umgang mit Tätern
- Politik (Österreich und allgemein), Schwerpunkt Lügner und Hetzer
- Genderwahnsinn
- Individualverkehr (in Wien)
- Schulsystem (ich bin Lehrer, „gefangen“ in einem maroden System)
Das konkrete Thema für jetzt:
Österreich ist ein Paradis für Täter. Täter werden mit Samthandschuhen angefasst. Fast niemand wird bei einer ersten kriminellen Handlung wirklich bestraft, das Zauberwort heißt „Bewährung“. Jedem Täter gibt man 10-20 Chancen.
Menschen, die sich wehren, werden definitiv bestraft und das auch noch mit höheren Strafen, „Notwehrüberschreitung“ nennen sie das. In vielen Fällen..

```html
<!DOCTYPE html>
<html lang="de">
<head>
<meta charset="utf-8">
<title>Der Zorn – Buchcover</title>
<link rel="stylesheet" href="https://fonts.googleapis.com/css2?family=Jost:wght@400&display=swap">
<style>
  :root {
    --backdrop: #d9b0a3;
    --cover-paper: #f4f4f3;
    --title-red: #e0103a;
    --title-navy: #0d1440;
    --fist-red: #b3232c;
    --fist-dark: #2a1416;
  }
  * { margin: 0; padding: 0; box-sizing: border-box; }
  html, body {
    width: 1200px;
    height: 937px;
    overflow: hidden;
    background: var(--backdrop);
  }
  .stage {
    position: relative;
    width: 1200px;
    height: 937px;
    display: flex;
    align-items: center;
    justify-content: center;
  }
  .book-cover {
    position: relative;
    width: 610px;
    height: 860px;
    background: var(--cover-paper);
    overflow: hidden;
    box-shadow: 0 20px 40px rgba(80, 40, 30, 0.25);
  }
  .cover-illustration {
    position: absolute;
    left: 180px;
    top: 55px;
    width: 340px;
    height: 690px;
    background: linear-gradient(180deg,
      rgba(179, 35, 44, 0.55) 0%,
      rgba(179, 35, 44, 0.45) 40%,
      rgba(42, 20, 22, 0.55) 62%,
      rgba(42, 20, 22, 0.15) 100%);
    border-radius: 46% 46% 30% 30% / 22% 22% 10% 10%;
  }
  .cover-title {
    position: absolute;
    inset: 0;
    font-family: "Jost", "Futura", sans-serif;
    font-weight: 400;
    line-height: 1;
  }
  .title-article {
    position: absolute;
    left: 58px;
    top: 362px;
    font-size: 250px;
    letter-spacing: -6px;
    color: var(--title-red);
  }
  .title-noun {
    position: absolute;
    left: 8px;
    top: 505px;
    font-size: 250px;
    letter-spacing: -14px;
    color: var(--title-navy);
    white-space: nowrap;
  }
</style>
</head>
<body>
  <main class="stage">
    <article class="book-cover">
      <div class="cover-illustration" role="img" aria-label="Gezeichnete, erhobene Faust in roten und schwarzen Schraffurstrichen"></div>
      <h1 class="cover-title">
        <span class="title-article">DER</span>
        <span class="title-noun">ZORN</span>
      </h1>
    </article>
  </main>
</body>
</html>
```